Buch-/eBook-Cover für Anbieter von Seminaren zu den Themen Deeskalation und Selbstschutz
Zielgruppe
Ich gebe mit KLW Seminare (KLW steht für Kraft Lebt Weiter) Seminare, überwiegend bei Behörden, Firmen, Institutionen und Rettungskräfte zu den Themen Deeskalation und Selbstschutz. Darüber hinaus gebe ich auch Vorträge zum o.g. Thema und biete Selbstverteidigungskurse u.a. für Frauen an. Zielgruppe des Buches sind grundsätzlich alle Menschen die sich unsicher fühlen. Nicht für Kinder, aber ab dem jugendlichen Alter aufwärts. Dieses Buchprojekt ist bereits mein zweites. Es gibt bereits ein Buch zu dem Thema, wobei das aktuelle Buchprojekt etwas 'tiefer' in die Materie geht. Das erste Buch heißt: Wanderer im offenen Gelände - Das Handbuch für gelassenes Auftreten in Streitmomenten www.klw-seminare.de
Aufgabenstellung
Das Farbkonzept von KLW (blau, orange, weiß) sollte erkennbar sein. (Wiedererkennung). Endformat des Buchs 12,5 x 19,0 cm, Umschlag: Softcover 4/4-farbig. https://www.papierwerk-blatt.de wird die Druckerei sein.
Buchtitel: Ruhe wohnt in dir selbst - Wie du Linien ziehst, Streit entschärfst und dich wappnest
Ich benötige nach dem Design die Daten, um sie an die Druckerei weiterzugeben. Geplant ist davon auch ein ebook. Ich benötige für den Druck den Buchdeckel vorne/hinten sowie Buchrücken und Strichcode mit ISBN-Nummer (wird gesondert übersandt) auf der Rückseite.
Das Design darf nicht zu überladen sein.

```html
<!DOCTYPE html>
<html lang="de">
<head>
<meta charset="utf-8">
<title>Ruhe wohnt in dir selbst – Umschlag</title>
<link rel="stylesheet" href="https://fonts.googleapis.com/css2?family=Bebas+Neue&family=Roboto:ital,wght@0,400;0,500;0,700;1,400&display=swap">
<style>
  :root {
    --navy: #1e3763;
    --navy-deep: #142746;
    --blue-glow: #2f5fa8;
    --orange: #e8690b;
    --white: #ffffff;
  }
  * { margin: 0; padding: 0; box-sizing: border-box; }
  html, body { width: 1200px; height: 877px; overflow: hidden; background: var(--navy); }
  .cover {
    position: relative; width: 1200px; height: 877px; overflow: hidden;
    font-family: "Roboto", sans-serif; color: var(--white);
  }
  .back {
    position: absolute; left: 0; top: 0; width: 577px; height: 877px;
    background: var(--navy);
  }
  .back-scene {
    position: absolute; left: 0; top: 430px; width: 577px; height: 447px;
    background: linear-gradient(180deg, rgba(30,55,99,0) 0%, rgba(47,95,168,0.35) 55%, rgba(20,39,70,0.6) 100%);
  }
  .back-heading {
    position: absolute; left: 42px; top: 84px;
    font-family: "Bebas Neue", sans-serif; font-size: 33px; line-height: 1; letter-spacing: 0.2px;
  }
  .accent { color: var(--orange); }
  .back-copy {
    position: absolute; left: 42px; top: 126px; width: 500px;
    font-size: 15.6px; line-height: 22.8px;
  }
  .back-copy p { margin-bottom: 22.8px; }
  .back-copy em { font-style: italic; }
  .back-copy .closing { font-weight: 500; }
  .back-copy .closing strong { font-weight: 700; }
  .isbn-box {
    position: absolute; left: 274px; top: 702px; width: 245px; height: 120px;
    background: var(--white);
  }
  .brand {
    position: absolute; display: flex; flex-direction: column; align-items: center;
  }
  .brand-ring {
    border: 2.5px solid var(--orange); border-radius: 50%;
  }
  .brand-name { font-weight: 700; color: var(--white); white-space: nowrap; }
  .brand-back { left: 48px; top: 728px; width: 158px; }
  .brand-back .brand-ring { width: 58px; height: 58px; }
  .brand-back .brand-name { font-size: 15px; margin-top: 14px; }
  .spine {
    position: absolute; left: 577px; top: 0; width: 46px; height: 877px;
    background: var(--orange);
  }
  .spine-text {
    position: absolute; left: 0; top: 88px; width: 46px; height: 375px;
    writing-mode: vertical-rl; transform: rotate(180deg);
    display: flex; align-items: center; justify-content: space-between;
    font-family: "Bebas Neue", sans-serif; font-size: 24px; line-height: 46px;
    white-space: nowrap;
  }
  .front {
    position: absolute; left: 623px; top: 0; width: 577px; height: 877px;
    background: var(--navy);
  }
  .front-scene {
    position: absolute; left: 0; top: 0; width: 577px; height: 877px;
    background:
      radial-gradient(ellipse 90px 200px at 290px 520px, rgba(232,105,11,0.75), rgba(232,105,11,0) 100%),
      radial-gradient(ellipse 420px 320px at 290px 560px, rgba(47,95,168,0.7), rgba(30,55,99,0) 100%),
      linear-gradient(180deg, var(--navy-deep) 0%, var(--navy) 40%, var(--navy-deep) 100%);
  }
  .author {
    position: absolute; left: 0; top: 47px; width: 577px; text-align: center;
    font-size: 26px; font-weight: 500; letter-spacing: 2px;
  }
  .title {
    position: absolute; left: 0; top: 86px; width: 577px; text-align: center;
    font-family: "Bebas Neue", sans-serif; font-size: 113px; line-height: 91px; font-weight: 400;
  }
  .subtitle {
    position: absolute; left: 0; top: 276px; width: 577px; text-align: center;
    font-size: 23px; line-height: 33px; letter-spacing: 0.3px;
  }
  .brand-front { left: 212px; top: 726px; width: 154px; }
  .brand-front .brand-ring { width: 72px; height: 72px; }
  .brand-front .brand-name { font-size: 18px; margin-top: 16px; }
</style>
</head>
<body>
<main class="cover">
  <section class="back">
    <div class="back-scene" role="img" aria-label="Abgedunkeltes Foto einer Menschenmenge aus blauen Figuren mit einer orangen Figur"></div>
    <h2 class="back-heading">Ruhe wohnt <span class="accent">in dir</span> selbst.</h2>
    <div class="back-copy">
      <p>Doch was, wenn der Alltag bedrohlich wird – verbal, körperlich<br>oder emotional?</p>
      <p>In einer Welt, in der Grenzen oft überschritten werden und<br>Eskalation jederzeit möglich ist, brauchst du mehr als Mut:<br>Du brauchst Werkzeuge. Dieses Buch gibt sie dir an die Hand.</p>
      <p>Nach seinem erfolgreichen Ratgeber <em>„Wanderer im offenen Gelände“</em><br>geht der Autor – erfahrener Praktiker mit realen Ausnahme-<br>situationen im Rücken – jetzt noch tiefer:<br>Du lernst, wie du früh erkennst, wenn sich eine Situation zuspitzt,<br>wie du Grenzen setzt, bevor sie überschritten werden, und wie du<br>dich selbst schützt – mit Haltung, Worten, rechtlichem Wissen und<br>im Ernstfall auch körperlich.</p>
      <p>Ob in Gesprächen, im Alltag, beruflich, auf der Straße oder in<br>Ausnahmemomenten: Dieses Buch zeigt dir, wie du handlungs-<br>fähig bleibst – und wieder wirst – in einer Welt, die nicht immer<br>friedlich ist.</p>
      <p class="closing"><strong>Denn echte Stärke beginnt nicht mit der Faust, sondern mit<br>Klarheit.</strong> Und mit dem tiefen Wissen: <strong class="accent">Ruhe wohnt in dir selbst.</strong></p>
    </div>
    <div class="brand brand-back">
      <span class="brand-ring"></span>
      <span class="brand-name">Kraft Lebt Weiter</span>
    </div>
    <div class="isbn-box" aria-label="Platz für ISBN-Strichcode"></div>
  </section>

  <aside class="spine">
    <div class="spine-text">
      <span>Jörg Lindner</span>
      <span>Ruhe wohnt in dir selbst</span>
    </div>
  </aside>

  <section class="front">
    <div class="front-scene" role="img" aria-label="Foto einer Menschenmenge aus blauen Figuren, in der Mitte eine leuchtend orange Figur"></div>
    <p class="author">JÖRG LINDNER</p>
    <h1 class="title">RUHE WOHNT<br><span class="accent">IN DIR</span> SELBST</h1>
    <p class="subtitle">Wie du Linien ziehst, Streit entschärfst<br>und dich wappnest</p>
    <div class="brand brand-front">
      <span class="brand-ring"></span>
      <span class="brand-name">Kraft Lebt Weiter</span>
    </div>
  </section>
</main>
</body>
</html>
```